Creative Frame Mat for 40Forge Challenge

I am gifting a present to my wife and am looking for your help to make it happen. I have a 8"x10" picture frame. In it, I want to place a 4"x6" picture. The rest of that space is the creative area I am looking for your help. Let's call it a picture border or mat. I don't care where the 4"x6" cut out for the picture is. You get to decide. The border or mat is to have a #40Forge theme. Images are below. You can incorporate some/all or add your own design.

Target Market(s)

Gym / health / self help enthusiast

Font styles to use
Sans Serif
Decorative

Requirements
Must have
• - Frame mat is 8" x 10"
- Include a cut out area for a picture to be inserted that is 4" x 6"
- A main header with "40FORGE"
Nice to have
• Color: Black, grey, white and red
Optional quotes to add in small text:
- I can do more
- Discipline
- Determination
- Perseverance
- Grit
- Confidence
- Self-Belief
- Self-Esteem
- Self-Worth

```html
<!DOCTYPE html>
<html lang="en">
<head>
<meta charset="utf-8">
<title>40Forge Frame Mat</title>
<link rel="stylesheet" href="https://fonts.googleapis.com/css2?family=Playfair+Display:wght@700;900&display=swap">
<style>
  :root {
    --ink: #000000;
    --tile: #111111;
    --paper: #ffffff;
    --red: #ff0000;
    --red-deep: #b30000;
    --grey: #8a8a8a;
    --icon: #dcdcdc;
    --flower: #7a0d0d;
  }
  html, body { margin: 0; padding: 0; overflow: hidden; background: var(--ink); }
  .mat {
    position: relative;
    width: 960px;
    height: 1200px;
    background: var(--ink);
    overflow: hidden;
    font-family: "Playfair Display", serif;
  }
  .dots { position: absolute; inset: 0; }
  .brand-main {
    position: absolute;
    left: 60px; top: 150px;
    width: 230px;
    display: flex; align-items: center; justify-content: center; gap: 12px;
    color: var(--paper);
    font-size: 40px; font-weight: 900; letter-spacing: 1px;
  }
  .brand-main .mark { width: 18px; height: 18px; background: var(--red); flex: none; }
  .brand-side {
    position: absolute;
    left: 718px; top: 140px;
    width: 160px;
    display: flex; align-items: center; justify-content: center; gap: 8px;
    color: var(--paper);
    font-size: 24px; font-weight: 900;
  }
  .brand-side .mark { width: 14px; height: 14px; border-radius: 50%; background: var(--red); flex: none; }
  .photo-backing, .photo-edge, .photo-window {
    position: absolute;
    width: 479px; height: 718px;
    left: 281px; top: 306px;
  }
  .photo-backing { background: var(--red); transform: rotate(-20deg); }
  .photo-edge { background: var(--red-deep); transform: rotate(-18deg); }
  .photo-window { background: var(--paper); transform: rotate(-15deg); }
  .habit {
    position: absolute;
    width: 114px; height: 86px;
    background: var(--tile);
    transform: rotate(-15deg);
    display: flex; align-items: center; justify-content: center;
  }
  .habit svg { width: 62px; height: 62px; fill: none; stroke: var(--icon); stroke-width: 2.4; stroke-linecap: round; stroke-linejoin: round; }
  .flower-art {
    position: absolute;
    left: 0; top: 915px;
    width: 234px; height: 251px;
    background: radial-gradient(ellipse at 55% 45%, var(--flower) 0%, rgba(122,13,13,0.35) 55%, rgba(0,0,0,0) 75%);
  }
  .motto {
    position: absolute;
    left: 484px; top: 1060px;
    margin: 0;
    color: var(--paper);
    font-size: 56px; font-weight: 700; letter-spacing: 3px;
    line-height: 1;
    white-space: nowrap;
    transform-origin: left bottom;
    transform: rotate(-18deg);
  }
</style>
</head>
<body>
<main class="mat">
  <svg class="dots" width="960" height="1200" viewBox="0 0 960 1200" aria-hidden="true">
    <g class="dots-top">
      <circle cx="531" cy="35" r="2.5" fill="#777"/><circle cx="552" cy="35" r="3" fill="#7d7d7d"/>
      <circle cx="573" cy="35" r="3.5" fill="#858585"/><circle cx="596" cy="35" r="4" fill="#8e8e8e"/>
      <circle cx="619" cy="35" r="4.8" fill="#999"/><circle cx="644" cy="35" r="5.4" fill="#a4a4a4"/>
      <circle cx="671" cy="35" r="6" fill="#b0b0b0"/><circle cx="699" cy="35" r="6.6" fill="#bcbcbc"/>
      <circle cx="729" cy="35" r="7.2" fill="#c8c8c8"/><circle cx="761" cy="35" r="7.8" fill="#d4d4d4"/>
      <circle cx="797" cy="35" r="8.4" fill="#e0e0e0"/><circle cx="835" cy="35" r="9" fill="#ebebeb"/>
      <circle cx="877" cy="35" r="9.8" fill="#f5f5f5"/><circle cx="924" cy="35" r="10.5" fill="#fff"/>
    </g>
    <g class="dots-right">
      <circle cx="925" cy="78" r="10" fill="#fff"/><circle cx="925" cy="119" r="10" fill="#fafafa"/>
      <circle cx="925" cy="159" r="9.6" fill="#f5f5f5"/><circle cx="925" cy="197" r="9.3" fill="#f0f0f0"/>
      <circle cx="925" cy="234" r="9" fill="#ebebeb"/><circle cx="925" cy="269" r="8.6" fill="#e6e6e6"/>
      <circle cx="925" cy="303" r="8.2" fill="#e0e0e0"/><circle cx="925" cy="336" r="7.8" fill="#dadada"/>
      <circle cx="925" cy="368" r="7.4" fill="#d4d4d4"/><circle cx="925" cy="400" r="7" fill="#cecece"/>
      <circle cx="925" cy="429" r="6.6" fill="#c8c8c8"/><circle cx="925" cy="458" r="6.2" fill="#c0c0c0"/>
      <circle cx="925" cy="486" r="5.8" fill="#b8b8b8"/><circle cx="925" cy="514" r="5.4" fill="#b0b0b0"/>
      <circle cx="925" cy="541" r="5" fill="#a8a8a8"/><circle cx="925" cy="567" r="4.6" fill="#a0a0a0"/>
      <circle cx="925" cy="593" r="4.2" fill="#989898"/><circle cx="925" cy="618" r="3.8" fill="#909090"/>
      <circle cx="925" cy="642" r="3.4" fill="#888"/><circle cx="925" cy="666" r="3" fill="#808080"/>
      <circle cx="925" cy="689" r="2.6" fill="#787878"/>
    </g>
    <g class="dots-left">
      <circle cx="35" cy="511" r="2.6" fill="#787878"/><circle cx="35" cy="534" r="3" fill="#808080"/>
      <circle cx="35" cy="557" r="3.4" fill="#888"/><circle cx="35" cy="582" r="3.8" fill="#909090"/>
      <circle cx="35" cy="607" r="4.2" fill="#989898"/><circle cx="35" cy="632" r="4.6" fill="#a0a0a0"/>
      <circle cx="35" cy="658" r="5" fill="#a8a8a8"/><circle cx="35" cy="685" r="5.4" fill="#b0b0b0"/>
      <circle cx="35" cy="712" r="5.8" fill="#b8b8b8"/><circle cx="35" cy="741" r="6.2" fill="#c0c0c0"/>
      <circle cx="35" cy="770" r="6.6" fill="#c8c8c8"/><circle cx="35" cy="800" r="7" fill="#cecece"/>
      <circle cx="35" cy="831" r="7.4" fill="#d4d4d4"/><circle cx="35" cy="863" r="7.8" fill="#dadada"/>
      <circle cx="35" cy="896" r="8.2" fill="#e0e0e0"/><circle cx="35" cy="930" r="8.6" fill="#e6e6e6"/>
      <circle cx="35" cy="965" r="9" fill="#ebebeb"/><circle cx="35" cy="1002" r="9.3" fill="#f0f0f0"/>
      <circle cx="35" cy="1039" r="9.6" fill="#f5f5f5"/><circle cx="35" cy="1078" r="10" fill="#fafafa"/>
      <circle cx="35" cy="1118" r="10" fill="#fff"/><circle cx="35" cy="1163" r="10.5" fill="#fff"/>
    </g>
    <g class="dots-bottom">
      <circle cx="82" cy="1163" r="10" fill="#fafafa"/><circle cx="124" cy="1163" r="9.4" fill="#f2f2f2"/>
      <circle cx="163" cy="1163" r="8.8" fill="#e8e8e8"/><circle cx="198" cy="1163" r="8.2" fill="#dedede"/>
      <circle cx="230" cy="1163" r="7.6" fill="#d2d2d2"/><circle cx="260" cy="1163" r="7" fill="#c6c6c6"/>
      <circle cx="289" cy="1163" r="6.4" fill="#bababa"/><circle cx="315" cy="1163" r="5.8" fill="#aeaeae"/>
      <circle cx="340" cy="1163" r="5.2" fill="#a2a2a2"/><circle cx="364" cy="1163" r="4.6" fill="#969696"/>
      <circle cx="386" cy="1163" r="4" fill="#8a8a8a"/><circle cx="408" cy="1163" r="3.3" fill="#808080"/>
      <circle cx="427" cy="1163" r="2.6" fill="#777"/>
    </g>
  </svg>

  <div class="brand-main"><span class="mark"></span><span>40FORGE</span></div>
  <div class="brand-side"><span class="mark"></span><span>40FORGE</span></div>

  <div class="photo-backing"></div>
  <div class="photo-edge"></div>
  <div class="photo-window" aria-label="4 by 6 inch photo opening"></div>

  <div class="habit" style="left:90px;top:536px" aria-label="Workout">
    <svg viewBox="0 0 60 60"><rect x="6" y="20" width="7" height="20" rx="3.5"/><rect x="13" y="16" width="7" height="28" rx="3.5"/><line x1="20" y1="30" x2="40" y2="30"/><rect x="40" y="16" width="7" height="28" rx="3.5"/><rect x="47" y="20" width="7" height="20" rx="3.5"/></svg>
  </div>
  <div class="habit" style="left:127px;top:675px" aria-label="Outdoor workout in any weather">
    <svg viewBox="0 0 60 60"><path d="M14 36 a9 9 0 0 1 2-17 a13 13 0 0 1 25 2 a8 8 0 0 1 4 15 z"/><line x1="18" y1="42" x2="24" y2="52"/><line x1="23" y1="42" x2="29" y2="52"/><path d="M36 44 l4 4 M40 44 l-4 4 M46 48 l3 3 M49 48 l-3 3"/></svg>
  </div>
  <div class="habit" style="left:164px;top:814px" aria-label="Follow a diet">
    <svg viewBox="0 0 60 60"><path d="M10 8 h22 l6 6 v38 h-28 z"/><line x1="15" y1="20" x2="32" y2="20"/><line x1="15" y1="26" x2="32" y2="26"/><line x1="15" y1="32" x2="30" y2="32"/><line x1="15" y1="38" x2="28" y2="38"/><circle cx="44" cy="44" r="9"/><path d="M44 35 q2 -5 6 -6"/></svg>
  </div>
  <div class="habit" style="left:201px;top:953px" aria-label="No alcohol">
    <svg viewBox="0 0 60 60"><path d="M27 6 h6 v12 l4 8 v28 h-14 v-28 l4 -8 z"/><line x1="14" y1="46" x2="46" y2="22"/></svg>
  </div>
  <div class="habit" style="left:704px;top:294px" aria-label="Drink water">
    <svg viewBox="0 0 60 60"><path d="M22 18 l10 18 a11 11 0 1 1 -20 0 z"/><path d="M38 8 l8 14 a8 8 0 1 1 -16 0 z"/><path d="M18 44 a5 5 0 0 0 5 4"/></svg>
  </div>
  <div class="habit" style="left:740px;top:430px" aria-label="Read">
    <svg viewBox="0 0 60 60"><path d="M30 16 q-10 -6 -22 -2 v30 q12 -4 22 2 z"/><path d="M30 16 q10 -6 22 -2 v30 q-12 -4 -22 2"/><path d="M5 18 v30 q13 -4 25 2 q12 -6 25 -2 v-30"/></svg>
  </div>
  <div class="habit" style="left:778px;top:567px" aria-label="Progress photo">
    <svg viewBox="0 0 60 60"><rect x="8" y="12" width="36" height="30" rx="1"/><path d="M44 20 l10 4 l-8 26 l-34 -8"/><circle cx="26" cy="23" r="5"/><path d="M16 40 q10 -12 20 0"/></svg>
  </div>

  <div class="flower-art" role="img" aria-label="Red line-drawn hibernating hibiscus flower with leaves"></div>

  <p class="motto">I can do more</p>
</main>
</body>
</html>
```